Simple Logo Design for Semi-Clear Plastic Frosted Card stock

Create a business card on frosted plastic. compliment existing logo elements with a tree trunk, roots, or seed at the lower half and the full logo both on the front.

Contact information will go on a solid portion of the back of this design since this card stock is semi-transparent.

It is important to consider this plastic card stock medium in your design. I found helpful tips and guides listed at velmarcards.example: be careful to understand ink printed on plastic cards cannot have too much of a consistent print area or risks peeling and fine lines can easily scratch off.
Updates

2" x 3.5" 20PT Clear Plastic Business cards with Round corners Please get info or templates here: https://www.velmarcards.example/product-detail/2-x-35-20pt-clear-plastic-business-cards-with-round-corners

Target Market(s)

Not for profit- religion

Industry/Entity Type

Business

Contact Information for Business Card

Must include complementary elements to the existing logo

Font styles to use
Decorative

Colors
000000

Requirements
Must have
• Elements of community, nature and oneness. Such as: seed, roots, tree trunk, etc.
• Three lines of space on the back for Name, Title, Phone Number.
Nice to have
• I like a light use of decorative elements
Should not have
• No eyes, from faces or animals.

```html
<!DOCTYPE html>
<html lang="en">
<head>
<meta charset="utf-8">
<title>Kindred Path – Business Card</title>
<link rel="stylesheet" href="https://fonts.googleapis.com/css2?family=Jost:wght@500;600&family=Arimo:wght@400;700&display=swap">
<style>
  :root {
    --backdrop: #e6e4e0;
    --card-top: rgba(244, 246, 247, 0.96);
    --card-bottom: rgba(226, 229, 231, 0.96);
    --card-edge: rgba(255, 255, 255, 0.9);
    --brand-green: #1f4a44;
    --mark-green: #2f6b35;
    --tagline: #1d3d38;
    --name-green: #1f4a2e;
    --ink-grey: #3a3a3a;
  }
  * { margin: 0; padding: 0; box-sizing: border-box; }
  html, body {
    width: 1200px;
    height: 969px;
    overflow: hidden;
    background: var(--backdrop);
  }
  .canvas {
    position: relative;
    width: 1200px;
    height: 969px;
  }
  .card {
    position: absolute;
    left: 188px;
    top: 275px;
    width: 825px;
    height: 468px;
    border-radius: 22px;
    background: linear-gradient(160deg, var(--card-top), var(--card-bottom));
    border: 2px solid var(--card-edge);
    box-shadow: 0 12px 30px rgba(0, 0, 0, 0.12);
    text-align: center;
  }
  .brand-dot {
    position: absolute;
    left: 50%;
    top: 70px;
    width: 120px;
    height: 120px;
    margin-left: -60px;
    border-radius: 50%;
    background: var(--mark-green);
  }
  .brand-name {
    position: absolute;
    left: 0;
    right: 0;
    top: 202px;
    font-family: "Jost", sans-serif;
    font-weight: 500;
    font-size: 50px;
    letter-spacing: 1px;
    color: var(--brand-green);
    line-height: 1;
    text-transform: uppercase;
  }
  .brand-tagline {
    position: absolute;
    left: 0;
    right: 0;
    top: 254px;
    font-family: "Jost", sans-serif;
    font-weight: 600;
    font-size: 15px;
    letter-spacing: 0.5px;
    color: var(--tagline);
    text-transform: uppercase;
  }
  .holder {
    position: absolute;
    left: 0;
    right: 0;
    top: 330px;
    font-family: "Arimo", sans-serif;
    color: var(--name-green);
  }
  .holder-name {
    font-weight: 700;
    font-size: 27px;
  }
  .holder-title {
    font-weight: 400;
    font-size: 23px;
  }
  .holder-phone {
    position: absolute;
    left: 0;
    right: 0;
    top: 388px;
    font-family: "Arimo", sans-serif;
    font-size: 25px;
    color: var(--ink-grey);
    letter-spacing: 0.5px;
  }
</style>
</head>
<body>
  <main class="canvas">
    <section class="card">
      <div class="brand-dot"></div>
      <h1 class="brand-name">Kindred Path</h1>
      <p class="brand-tagline">Wisdom, Fellowship &amp; Harmony</p>
      <p class="holder"><span class="holder-name">Marcus Hale -</span> <span class="holder-title">President</span></p>
      <p class="holder-phone">555 0142 7789</p>
    </section>
  </main>
</body>
</html>
```